App Redesign for PathMentor

We're looking for a skilled UI/UX designer to modernize the PathMentor mobile app, enhancing user engagement while preserving our current brand identity.

Key Objectives:
Refresh the app using modern design trends
Maintain a clean, calm, and playful aesthetic aligned with our brand
Boost engagement through improved flow, visuals, and interactivity

Design Requirements:
Retain recognizability from our app and website (see Brand ID Guide) (and website pathmentorhub.example)
Reflect a tone that is supportive, fun/ playful, and professional

Design 5–8 key screens, including:
Home/Dashboard
Daily Intentions Interface
Gamification Overview (Streaks, Rewards)
Social Features (Direct Realtime Feedback, Messaging, Challenges)
Progress Tracking

New Feature Concepts to Include:
Daily Intentions with voice/text input and visual encouragement
Gamification elements like streaks, badges, and animations
Social Connections including messaging, reactions, and feedback tools
Optional: Subtle design cues for future AI-driven interactions

Audience: Adults aged 25–55 interested in personal development and coaching. Tech-comfortable but not tech-savvy.

Visual Inspiration: Lexaroo (gamification), Calmnook (intentions), Pacely (social support)

Target Market(s)

Corporate Leaders and Entrepreneurs

Industry/Entity Type

Leadership Training & Consultancies

Font styles to use
Sans Serif
Other font styles liked:
• Avenir, Arial

Colors
FFF300
FFF600
FEFA6F
FFFEC7
FFFEE8

Requirements
Nice to have
• Lexaroo, Calmnook,

```html
<!DOCTYPE html>
<html lang="en">
<head>
<meta charset="utf-8">
<title>PathMentor — App Screens</title>
<link rel="stylesheet" href="https://fonts.googleapis.com/css2?family=Figtree:wght@400;500;600;700;900&display=swap">
<style>
:root{
  --bg:#8eacd6;
  --yellow:#ffd600;
  --yellow-soft:#fff6b3;
  --orange:#f5a623;
  --ink:#111111;
  --muted:#8a8a8a;
  --line:#dcdcdc;
  --card:#eeeeee;
  --white:#ffffff;
}
*{margin:0;padding:0;box-sizing:border-box}
html,body{width:1117px;height:1200px;overflow:hidden;background:var(--bg)}
body{font-family:"Figtree",Arial,sans-serif;color:var(--ink)}
.stage{position:absolute;left:0;top:0;width:1850px;height:1988px;transform:scale(0.60378);transform-origin:0 0}
.screen{position:absolute;width:422px;background:var(--white);overflow:hidden}
.screen > *{position:absolute}
.status{left:29px;right:29px;top:20px;height:20px;display:flex;justify-content:space-between;align-items:center;font-size:17px;font-weight:500}
.status svg{width:56px;height:14px}
.header-band{left:0;top:0;width:100%;height:132px;background:var(--yellow)}
.title{left:30px;top:72px;font-size:25px;font-weight:500}
.tabbar{left:30px;width:363px;height:62px;background:#000;border-radius:8px;display:flex;justify-content:space-around;align-items:center;padding:0 8px}
.tabbar a{color:var(--white);font-size:13px;display:flex;flex-direction:column;align-items:center;gap:3px;text-decoration:none}
.tabbar a.active{color:var(--yellow)}
.tabbar svg{width:18px;height:18px}
.fab{width:66px;height:66px;border-radius:50%;background:var(--yellow);box-shadow:0 6px 14px rgba(0,0,0,.18);display:flex;align-items:center;justify-content:center}
.fab svg{width:30px;height:30px}
/* rewards */
.reward{left:30px;width:363px;height:103px}
.reward > *{position:absolute}
.reward .crown{left:0;top:14px;width:56px;height:42px}
.reward h3{left:76px;top:8px;font-size:14px;font-weight:500}
.reward p{left:76px;top:30px;font-size:11.5px;line-height:15px;width:160px}
.reward .pts{right:22px;top:30px;font-size:23px}
.reward hr{left:8px;right:8px;top:84px;border:0;border-top:1.5px solid var(--line)}
/* chat */
.chat-name{left:116px;top:70px;font-size:18px;font-weight:500}
.chat-state{left:116px;top:94px;font-size:12px;color:#a58a00}
.avatar{border-radius:50%}
.stamp{font-size:7px;color:#555;width:257px;text-align:right}
.bubble{width:257px;height:66px;padding:11px 16px;font-size:11.5px;line-height:15.5px;border-radius:4px}
.bubble.them{background:#000;color:var(--white)}
.bubble.me{background:#d6d6d6;color:#333}
.composer{left:67px;top:870px;width:242px;height:45px;border-radius:12px;background:#f3f3f3;font-size:13px;color:var(--muted);padding:14px 14px}
.tool{width:26px;height:26px}
/* streaks */
.big-num{left:0;width:100%;top:255px;text-align:center;font-size:200px;font-weight:900;line-height:200px;color:var(--yellow);-webkit-text-stroke:7px var(--orange)}
.streak-label{left:0;width:100%;top:446px;text-align:center;font-size:34px}
.day-labels{font-size:11px;color:#444;text-align:center;width:40px}
.streak-note{left:0;width:100%;top:608px;text-align:center;font-size:16px;line-height:20px}
/* daily interactions */
.day-box{width:104px;height:82px;font-size:24px;font-weight:500;display:flex;align-items:center;justify-content:center;border-radius:3px}
.day-box.past{background:#ebebeb;border:1.5px solid #ffe36b}
.day-box.next{background:var(--white);border:1.5px solid #000}
.day-text{font-size:15.5px;line-height:19.5px;width:200px}
.day-text.right{text-align:right}
/* tracking coach */
.user-chip{right:30px;top:78px;display:flex;align-items:center;gap:8px;font-size:12px}
.user-chip span.dot{width:30px;height:30px;border-radius:50%;background:var(--yellow-soft);display:flex;align-items:center;justify-content:center}
.welcome{left:30px;top:125px;width:363px;height:121px;background:var(--card);border-radius:6px}
.welcome > *{position:absolute}
.cta{top:260px;width:177px;height:59px;border-radius:3px;padding:12px 14px;font-size:16px;font-weight:600;line-height:17px}
.cta .pill{position:absolute;right:14px;top:20px;font-size:11px;font-weight:500;padding:3px 12px;border-radius:10px}
.panel{left:30px;width:363px;background:var(--white);border-radius:6px;box-shadow:0 2px 10px rgba(0,0,0,.12)}
.panel h2{position:absolute;left:16px;font-size:19px;font-weight:500}
.growth h3{left:46px;font-size:16px;font-weight:600}
.growth-q{left:46px;font-size:13px;line-height:18px;color:#333;width:170px}
.legend{left:46px;display:flex;gap:8px;font-size:7px;color:#666}
.legend i{display:inline-block;width:7px;height:7px;margin-right:2px;vertical-align:-1px}
.divider{left:38px;width:347px;border-top:1.5px solid var(--line)}
</style>
</head>
<body>
<svg width="0" height="0" style="position:absolute" aria-hidden="true">
  <defs>
    <symbol id="i-status" viewBox="0 0 56 14">
      <rect x="0" y="9" width="3" height="4" rx="1" fill="#000"/><rect x="4.5" y="7" width="3" height="6" rx="1" fill="#000"/><rect x="9" y="4.5" width="3" height="8.5" rx="1" fill="#000"/><rect x="13.5" y="2" width="3" height="11" rx="1" fill="#000"/>
      <path d="M22 5.5a10 10 0 0 1 14 0M24.5 8a6.5 6.5 0 0 1 9 0M27 10.5a3 3 0 0 1 4 0" stroke="#000" stroke-width="2" fill="none" stroke-linecap="round"/>
      <rect x="39" y="2" width="14" height="9" rx="2" fill="#000"/><rect x="54" y="5" width="1.5" height="3.5" rx=".7" fill="#000"/>
    </symbol>
    <symbol id="i-home" viewBox="0 0 24 24"><path d="M4 11 12 4l8 7v9h-5v-6H9v6H4z" fill="none" stroke="currentColor" stroke-width="2" stroke-linejoin="round"/></symbol>
    <symbol id="i-sliders" viewBox="0 0 24 24"><g stroke="currentColor" stroke-width="2" stroke-linecap="round"><path d="M4 6h16M4 12h16M4 18h16"/><circle cx="9" cy="6" r="2" fill="#000"/><circle cx="15" cy="12" r="2" fill="#000"/><circle cx="8" cy="18" r="2" fill="#000"/></g></symbol>
    <symbol id="i-edit" viewBox="0 0 24 24"><g fill="none" stroke="currentColor" stroke-width="2" stroke-linejoin="round" stroke-linecap="round"><path d="M18 13v7H4V6h7"/><path d="M17 3l4 4-9 9H8v-4z"/><path d="M7 18h6"/></g></symbol>
    <symbol id="i-chart" viewBox="0 0 24 24"><g fill="none" stroke="currentColor" stroke-width="2" stroke-linejoin="round" stroke-linecap="round"><path d="M3 4v17h18"/><path d="M6 15l5-5 3 3 6-6"/></g></symbol>
    <symbol id="i-chat" viewBox="0 0 30 30"><path d="M4 6a4 4 0 0 1 4-4h14a4 4 0 0 1 4 4v11a4 4 0 0 1-4 4h-5l-5 5v-5H8a4 4 0 0 1-4-4z" fill="#000"/><path d="M10 10h10M10 14h7" stroke="#ffd600" stroke-width="2.2" stroke-linecap="round"/></symbol>
    <symbol id="i-crown" viewBox="0 0 56 42"><path d="M4 10l12 12 12-18 12 18 12-12-4 24H8z" fill="#ffc400"/><circle cx="4" cy="9" r="3.5" fill="#ffc400"/><circle cx="28" cy="4" r="3.5" fill="#ffc400"/><circle cx="52" cy="9" r="3.5" fill="#ffc400"/><rect x="7" y="32" width="42" height="8" rx="4" fill="#f59a1b"/></symbol>
    <symbol id="i-tick" viewBox="0 0 36 36"><circle cx="18" cy="18" r="17" fill="#ffd600" stroke="#f5c000"/><path d="M12 18l4 4 8-8" stroke="#f0a000" stroke-width="1.8" fill="none" stroke-linecap="round"/></symbol>
    <symbol id="i-rings" viewBox="0 0 100 100"><g fill="none" stroke-width="3" stroke-linecap="round"><circle cx="50" cy="50" r="46" stroke="#f6b24a" stroke-dasharray="250 40" transform="rotate(-80 50 50)"/><circle cx="50" cy="50" r="40" stroke="#f5a623" stroke-dasharray="200 60" transform="rotate(-60 50 50)"/><circle cx="50" cy="50" r="34" stroke="#fbd36b" stroke-dasharray="170 60" transform="rotate(-100 50 50)"/><circle cx="50" cy="50" r="28" stroke="#f3c24c" stroke-dasharray="140 40" transform="rotate(-90 50 50)"/></g></symbol>
  </defs>
</svg>

<main class="stage">

  <!-- Rewards -->
  <section class="screen rewards" style="left:49px;top:44px;height:939px">
    <div class="status"><span>9:41</span><svg><use href="#i-status"/></svg></div>
    <h1 class="title">Rewards</h1>
    <div class="reward" style="top:128px"><svg class="crown"><use href="#i-crown"/></svg><h3>Lorem ipsum</h3><p>Lorem ipsum dolor sit amet, consectetur adipiscing elit.</p><span class="pts">80 pts</span><hr></div>
    <div class="reward" style="top:231px"><svg class="crown"><use href="#i-crown"/></svg><h3>Lorem ipsum</h3><p>Lorem ipsum dolor sit amet, consectetur adipiscing elit.</p><span class="pts">80 pts</span><hr></div>
    <div class="reward" style="top:334px"><svg class="crown"><use href="#i-crown"/></svg><h3>Lorem ipsum</h3><p>Lorem ipsum dolor sit amet, consectetur adipiscing elit.</p><span class="pts">80 pts</span><hr></div>
    <div class="reward" style="top:437px"><svg class="crown"><use href="#i-crown"/></svg><h3>Lorem ipsum</h3><p>Lorem ipsum dolor sit amet, consectetur adipiscing elit.</p><span class="pts">80 pts</span><hr></div>
    <div class="reward" style="top:540px"><svg class="crown"><use href="#i-crown"/></svg><h3>Lorem ipsum</h3><p>Lorem ipsum dolor sit amet, consectetur adipiscing elit.</p><span class="pts">80 pts</span><hr></div>
    <div class="reward" style="top:643px"><svg class="crown"><use href="#i-crown"/></svg><h3>Lorem ipsum</h3><p>Lorem ipsum dolor sit amet, consectetur adipiscing elit.</p><span class="pts">80 pts</span></div>
    <div class="fab" style="left:327px;top:760px"><svg><use href="#i-chat"/></svg></div>
    <nav class="tabbar" style="top:851px">
      <a><svg><use href="#i-home"/></svg>Home</a><a class="active"><svg><use href="#i-sliders"/></svg>Interactions</a><a><svg><use href="#i-edit"/></svg>Questions</a><a><svg><use href="#i-chart"/></svg>Reports</a>
    </nav>
  </section>

  <!-- Chat -->
  <section class="screen chat" style="left:493px;top:44px;height:939px">
    <div class="header-band"></div>
    <div class="status"><span>9:41</span><svg><use href="#i-status"/></svg></div>
    <svg style="left:24px;top:80px;width:18px;height:18px" viewBox="0 0 18 18"><path d="M16 9H3M8 4 3 9l5 5" stroke="#000" stroke-width="1.8" fill="none" stroke-linecap="round" stroke-linejoin="round"/></svg>
    <div class="avatar" role="img" aria-label="Coach profile photo" style="left:59px;top:67px;width:44px;height:44px;background:radial-gradient(circle at 50% 40%,#c9a27c,#3a2a20)"></div>
    <div style="left:94px;top:98px;width:10px;height:10px;border-radius:50%;background:#2ecc71;border:2px solid var(--yellow)"></div>
    <div class="chat-name">Milo Harte</div>
    <div class="chat-state">Active now</div>

    <div class="stamp" style="left:26px;top:158px">11:15am, Sun</div>
    <div class="bubble them" style="left:26px;top:175px">Lorem ipsum dolor sit amet, consectetur adipiscing elit. Lorem ipsum dolor sit amet, consectetur adipiscing elit.</div>
    <svg style="left:40px;top:240px;width:20px;height:16px" viewBox="0 0 20 16"><path d="M0 0h20L0 16z" fill="#000"/></svg>

    <div class="stamp" style="left:-78px;top:266px">11:15am, Sun</div>
    <div class="bubble me" style="left:133px;top:282px">Lorem ipsum dolor sit amet, consectetur adipiscing elit. Lorem ipsum dolor sit amet, consectetur adipiscing elit.</div>
    <svg style="left:356px;top:347px;width:20px;height:16px" viewBox="0 0 20 16"><path d="M0 0h20v16z" fill="#d6d6d6"/></svg>

    <div class="stamp" style="left:26px;top:373px">11:15am, Sun</div>
    <div class="bubble them" style="left:26px;top:389px">Lorem ipsum dolor sit amet, consectetur adipiscing elit. Lorem ipsum dolor sit amet, consectetur adipiscing elit.</div>
    <svg style="left:40px;top:454px;width:20px;height:16px" viewBox="0 0 20 16"><path d="M0 0h20L0 16z" fill="#000"/></svg>

    <div style="left:0;top:847px;width:100%;border-top:1px solid #eee"></div>
    <svg class="tool" style="left:27px;top:879px" viewBox="0 0 24 24"><path d="M20 11l-8 8a5 5 0 0 1-7-7l9-9a3.3 3.3 0 0 1 5 5l-9 9a1.7 1.7 0 0 1-2.5-2.5l8-8" fill="none" stroke="#222" stroke-width="1.6" stroke-linecap="round"/></svg>
    <div class="composer">Write your message</div>
    <svg style="left:274px;top:880px;width:24px;height:24px" viewBox="0 0 24 24"><rect x="7" y="3" width="13" height="15" rx="3" fill="none" stroke="#999" stroke-width="1.5"/><rect x="4" y="6" width="13" height="15" rx="3" fill="#f3f3f3" stroke="#999" stroke-width="1.5"/></svg>
    <svg class="tool" style="left:327px;top:879px" viewBox="0 0 24 24"><path d="M3 8h4l2-3h6l2 3h4v12H3z" fill="none" stroke="#222" stroke-width="1.6" stroke-linejoin="round"/><circle cx="12" cy="13" r="4" fill="none" stroke="#222" stroke-width="1.6"/></svg>
    <svg class="tool" style="left:368px;top:879px" viewBox="0 0 24 24"><rect x="8.5" y="2" width="7" height="13" rx="3.5" fill="none" stroke="#222" stroke-width="1.6"/><path d="M5 11a7 7 0 0 0 14 0M12 18v4" fill="none" stroke="#222" stroke-width="1.6" stroke-linecap="round"/></svg>
  </section>

  <!-- Streaks -->
  <section class="screen streaks" style="left:493px;top:1005px;height:939px">
    <div class="status"><span>9:41</span><svg><use href="#i-status"/></svg></div>
    <h1 class="title">Streaks</h1>
    <div class="big-num">3</div>
    <div class="streak-label">Days Streak</div>
    <svg style="left:55px;top:517px;width:312px;height:36px" viewBox="0 0 312 36">
      <use href="#i-tick" x="0" y="0" width="36" height="36"/>
      <use href="#i-tick" x="46" y="0" width="36" height="36"/>
      <use href="#i-tick" x="92" y="0" width="36" height="36"/>
      <circle cx="156" cy="18" r="18" fill="#ececec"/><circle cx="202" cy="18" r="18" fill="#ececec"/><circle cx="247" cy="18" r="18" fill="#ececec"/><circle cx="293" cy="18" r="18" fill="#ececec"/>
    </svg>
    <div class="day-labels" style="left:53px;top:564px">Mon</div>
    <div class="day-labels" style="left:99px;top:564px">Tues</div>
    <div class="day-labels" style="left:145px;top:564px">Wed</div>
    <div class="day-labels" style="left:191px;top:564px">Thu</div>
    <div class="day-labels" style="left:237px;top:564px">Fri</div>
    <div class="day-labels" style="left:282px;top:564px">Sat</div>
    <div class="day-labels" style="left:328px;top:564px">Sun</div>
    <p class="streak-note">Keep the momentum going! Performe<br>tomorrow to maintain your streak.</p>
    <div class="fab" style="left:327px;top:760px"><svg><use href="#i-chat"/></svg></div>
    <nav class="tabbar" style="top:851px">
      <a><svg><use href="#i-home"/></svg>Home</a><a class="active"><svg><use href="#i-sliders"/></svg>Interactions</a><a><svg><use href="#i-edit"/></svg>Questions</a><a><svg><use href="#i-chart"/></svg>Reports</a>
    </nav>
  </section>

  <!-- Daily Interactions -->
  <section class="screen daily" style="left:936px;top:44px;height:1214px">
    <div class="header-band"></div>
    <div class="status"><span>9:41</span><svg><use href="#i-status"/></svg></div>
    <h1 class="title">Daily Interactions</h1>
    <svg style="left:0;top:0;width:422px;height:1100px" viewBox="0 0 422 1100">
      <g fill="none" stroke="#222" stroke-width="1" stroke-dasharray="3 3">
        <path d="M82 280v14h250v14"/>
        <path d="M82 414v14h250v-14"/>
        <path d="M82 548v14h250v14"/>
        <path d="M82 682v14h250v-14"/>
        <path d="M82 816v14h250v14"/>
        <path d="M82 950v14h250v-14"/>
      </g>
    </svg>
    <div class="day-box past" style="left:30px;top:184px">Day 1</div>
    <p class="day-text" style="left:155px;top:195px">Lorem ipsum dolor sit amet, consectetur adipiscing elit. Quisque sed aliquet sem.</p>
    <div class="day-box next" style="left:288px;top:318px">Day 2</div>
    <p class="day-text right" style="left:66px;top:329px">Lorem ipsum dolor sit amet, consectetur adipiscing elit. Quisque sed aliquet sem.</p>
    <div class="day-box past" style="left:30px;top:452px">Day 3</div>
    <p class="day-text" style="left:155px;top:463px">Lorem ipsum dolor sit amet, consectetur adipiscing elit. Quisque sed aliquet sem.</p>
    <div class="day-box next" style="left:288px;top:586px">Day 4</div>
    <p class="day-text right" style="left:66px;top:597px">Lorem ipsum dolor sit amet, consectetur adipiscing elit. Quisque sed aliquet sem.</p>
    <div class="day-box past" style="left:30px;top:721px">Day 5</div>
    <p class="day-text" style="left:155px;top:732px">Lorem ipsum dolor sit amet, consectetur adipiscing elit. Quisque sed aliquet sem.</p>
    <div class="day-box next" style="left:288px;top:855px">Day 6</div>
    <p class="day-text right" style="left:66px;top:866px">Lorem ipsum dolor sit amet, consectetur adipiscing elit. Quisque sed aliquet sem.</p>
    <div class="day-box past" style="left:30px;top:989px">Day 7</div>
    <p class="day-text" style="left:155px;top:1000px">Lorem ipsum dolor sit amet, consectetur adipiscing elit. Quisque sed aliquet sem.</p>
    <div class="fab" style="left:327px;top:1028px"><svg><use href="#i-chat"/></svg></div>
    <nav class="tabbar" style="top:1118px">
      <a><svg><use href="#i-home"/></svg>Home</a><a class="active"><svg><use href="#i-sliders"/></svg>Interactions</a><a><svg><use href="#i-edit"/></svg>Questions</a><a><svg><use href="#i-chart"/></svg>Reports</a>
    </nav>
  </section>

  <!-- Tracking Coach dashboard -->
  <section class="screen coach" style="left:1379px;top:44px;height:1350px">
    <div class="status"><span>9:41</span><svg><use href="#i-status"/></svg></div>
    <h1 class="title">Tracking Coach</h1>
    <div class="user-chip">Jane Doe <span class="dot"><svg width="14" height="16" viewBox="0 0 14 16"><circle cx="7" cy="4.5" r="3.5" fill="#ffd600"/><path d="M0 16a7 6 0 0 1 14 0z" fill="#ffd600"/></svg></span></div>

    <div class="welcome">
      <div style="left:16px;top:18px;font-size:16px">Welcome</div>
      <div style="left:16px;top:37px;font-size:20px;font-weight:500">Jane Doe</div>
      <div style="left:16px;top:66px;font-size:11.5px;line-height:15px;color:#333">Track your overall progress<br>and take your mission further!</div>
      <div role="img" aria-label="Member profile photo" style="left:256px;top:14px;width:90px;height:90px;border-radius:50%;background:radial-gradient(circle at 50% 45%,#f6d0c4,#f19aa6)"></div>
    </div>

    <div class="cta" style="left:30px;background:var(--yellow)">Daily<br>Intentions<span class="pill" style="background:#ffe97a">Let's Go!</span></div>
    <div class="cta" style="left:216px;background:#000;color:#fff">Streak<br>Goal<span class="pill" style="background:#555;color:#ddd">Set Goal</span></div>

    <div class="panel" style="top:344px;height:154px">
      <h2 style="top:18px">Weekly Progress</h2>
      <svg style="position:absolute;left:14px;top:64px;width:340px;height:40px" viewBox="0 0 340 40">
        <g fill="none" stroke-width="1.5">
          <circle cx="20" cy="19" r="17" stroke="#e3e3e3"/><circle cx="20" cy="19" r="17" stroke="#ffd600" stroke-dasharray="60 107" transform="rotate(-90 20 19)"/>
          <circle cx="70" cy="19" r="17" stroke="#e3e3e3"/>
          <circle cx="119" cy="19" r="17" stroke="#e3e3e3"/><circle cx="119" cy="19" r="17" stroke="#ffd600" stroke-dasharray="80 107" transform="rotate(-90 119 19)"/>
          <circle cx="167" cy="19" r="17" stroke="#e3e3e3"/><circle cx="167" cy="19" r="17" stroke="#ffd600" stroke-dasharray="25 107" transform="rotate(-90 167 19)"/>
          <circle cx="216" cy="19" r="17" stroke="#ffd600" stroke-width="2"/>
          <circle cx="265" cy="19" r="17" stroke="#e3e3e3"/><circle cx="265" cy="19" r="17" stroke="#ffd600" stroke-dasharray="90 107" transform="rotate(-90 265 19)"/>
          <circle cx="314" cy="19" r="17" stroke="#e3e3e3"/><circle cx="314" cy="19" r="17" stroke="#ffd600" stroke-dasharray="40 107" transform="rotate(-90 314 19)"/>
        </g>
        <g></g>
      </svg>
      <svg style="position:absolute;left:14px;top:108px;width:340px;height:14px" viewBox="0 0 340 14">
        <g font-family="Figtree, Arial, sans-serif" font-size="11" fill="#444" text-anchor="middle">
          <text x="20" y="11">Mon</text><text x="70" y="11">Tues</text><text x="119" y="11">Wed</text><text x="167" y="11">Thu</text><text x="216" y="11">Fri</text><text x="265" y="11">Sat</text><text x="314" y="11">Sun</text>
        </g>
      </svg>
    </div>

    <div class="panel" style="top:530px;height:211px">
      <h2 style="top:16px">Your Overall Progress</h2>
      <svg style="position:absolute;left:0;top:0;width:363px;height:211px" viewBox="30 530 363 211">
        <defs>
          <linearGradient id="area" x1="0" y1="0" x2="0" y2="1"><stop offset="0" stop-color="#ffd600" stop-opacity=".85"/><stop offset="1" stop-color="#fff6b3" stop-opacity=".5"/></linearGradient>
        </defs>
        <g font-family="Figtree, Arial, sans-serif" font-size="9" fill="#666" text-anchor="end">
          <text x="78" y="597">100</text><text x="78" y="620">80</text><text x="78" y="642">60</text><text x="78" y="665">40</text><text x="78" y="687">20</text><text x="78" y="710">0</text>
        </g>
        <path d="M86 594v114h277" fill="none" stroke="#ddd" stroke-width="1"/>
        <path d="M86 650C98 645 104 640 112 642S124 654 132 650 152 640 158 628 166 604 172 608 182 646 192 660 206 640 216 632 230 608 238 612 254 630 262 632 276 656 286 654 300 640 310 630 336 616 344 611V708H86Z" fill="url(#area)"/>
        <path d="M86 650C98 645 104 640 112 642S124 654 132 650 152 640 158 628 166 604 172 608 182 646 192 660 206 640 216 632 230 608 238 612 254 630 262 632 276 656 286 654 300 640 310 630 336 616 344 611" fill="none" stroke="#ffd600" stroke-width="3" stroke-linecap="round"/>
      </svg>
    </div>

    <h2 style="left:46px;top:778px;font-size:24px;font-weight:500">Your Growth</h2>

    <h3 class="growth" style="left:46px;top:826px;font-size:16px;font-weight:600">Body</h3>
    <p class="growth-q" style="top:855px">Did I take a cold shower or swim in the river today?</p>
    <div class="legend" style="top:902px"><span><i style="background:#f5a623"></i>Week 1</span><span><i style="background:#fbd36b"></i>Week 2</span><span><i style="background:#f08a3e"></i>Week 3</span><span><i style="background:#f3c24c"></i>Week 4</span></div>
    <svg style="left:260px;top:821px;width:96px;height:96px"><use href="#i-rings"/></svg>
    <div class="divider" style="top:934px"></div>

    <h3 style="left:46px;top:968px;font-size:16px;font-weight:600">Balance</h3>
    <p class="growth-q" style="top:997px">What was focus in family activities</p>
    <div class="legend" style="top:1043px"><span><i style="background:#f5a623"></i>Week 1</span><span><i style="background:#fbd36b"></i>Week 2</span><span><i style="background:#f08a3e"></i>Week 3</span><span><i style="background:#f3c24c"></i>Week 4</span></div>
    <svg style="left:268px;top:963px;width:96px;height:96px;transform:rotate(40deg)"><use href="#i-rings"/></svg>
    <div class="divider" style="top:1087px"></div>

    <h3 style="left:46px;top:1110px;font-size:16px;font-weight:600">Business</h3>
    <p class="growth-q" style="top:1139px">Did I chunk my day and defined my Big 3</p>
    <div class="legend" style="top:1185px"><span><i style="background:#f5a623"></i>Week 1</span><span><i style="background:#fbd36b"></i>Week 2</span><span><i style="background:#f08a3e"></i>Week 3</span><span><i style="background:#f3c24c"></i>Week 4</span></div>
    <svg style="left:260px;top:1105px;width:96px;height:96px;transform:rotate(-30deg)"><use href="#i-rings"/></svg>

    <div class="fab" style="left:327px;top:1173px"><svg><use href="#i-chat"/></svg></div>
    <nav class="tabbar" style="top:1264px">
      <a><svg><use href="#i-home"/></svg>Home</a><a class="active"><svg><use href="#i-sliders"/></svg>Interactions</a><a><svg><use href="#i-edit"/></svg>Questions</a><a><svg><use href="#i-chart"/></svg>Reports</a>
    </nav>
  </section>

</main>
</body>
</html>
```